Elegant One-Page Flyer That Catches People's Eye

For a series of workshops and zoom calls I am marketing with a colleague of mine, we would like to have an elegant, catchy one-page flyer that entices people to contact us. I am envisioning a one-page flyer (a card that is somewhat larger than a postcard) with great text, layout and images which magnetically draws people to us and is positive and inspiring. Also, if at all possible, a QR code linking it to our websites. Good colours would be shades of blue and green. I am uploading: the Text, our pictures, logos and contact information.

```html
<!DOCTYPE html>
<html lang="en">
<head>
<meta charset="utf-8">
<title>Rising above Hidden Career Deal Breakers</title>
<link rel="stylesheet" href="https://fonts.googleapis.com/css2?family=Nunito:wght@800;900&family=Raleway:wght@300;400&family=Josefin+Sans:wght@300;600&display=swap">
<style>
  :root {
    --teal: #2bc9a8;
    --teal-dark: #21b799;
    --blue: #00b6e4;
    --blue-deep: #0a8fd8;
    --cyan: #1fc3c9;
    --pale: #efefef;
    --white: #ffffff;
    --green-light: #93dc8a;
  }
  html, body { margin: 0; padding: 0; overflow: hidden; background: var(--white); }
  .flyer {
    position: relative;
    width: 1200px;
    height: 2200px;
    overflow: hidden;
    background: var(--white);
    color: var(--white);
    font-family: "Raleway", sans-serif;
  }
  .shapes { position: absolute; inset: 0; }
  .block { position: absolute; margin: 0; }

  .hook { left: 73px; top: 38px; font-weight: 400; line-height: 1.27; }
  .hook p { margin: 0; white-space: nowrap; }
  .hook .q { font-size: 33px; }
  .hook .feel { font-size: 37px; }
  .hook strong { font-family: "Nunito", sans-serif; font-weight: 900; }

  .format {
    left: 684px; top: 260px; width: 300px; text-align: center;
    font-family: "Josefin Sans", sans-serif; font-weight: 300; font-size: 25px; line-height: 40px;
  }
  .format strong { font-weight: 600; }

  .promise { left: 675px; top: 584px; width: 440px; }
  .promise h2 {
    margin: 0 0 30px; font-family: "Nunito", sans-serif; font-weight: 800;
    font-size: 27px; line-height: 33px; white-space: nowrap;
  }
  .promise ul { margin: 0; padding: 0; list-style: none; font-size: 27px; line-height: 33px; }
  .promise li { position: relative; margin-bottom: 6px; white-space: nowrap; }
  .promise li::before { content: "•"; position: absolute; left: -20px; }

  .section-title {
    left: 79px; top: 1066px; color: var(--cyan);
    font-family: "Nunito", sans-serif; font-weight: 900; font-size: 37px;
  }
  .section-rule { position: absolute; left: 79px; top: 1117px; width: 51px; height: 2px; background: var(--cyan); }

  .bio-name { font-family: "Nunito", sans-serif; font-weight: 900; font-size: 31px; margin: 0 0 30px; }
  .bio-text { font-size: 27px; line-height: 33px; font-weight: 400; margin: 0; white-space: nowrap; }
  .bio-nora { left: 472px; top: 1288px; width: 680px; }
  .bio-helena { left: 339px; top: 1742px; width: 410px; }

  .brand {
    position: absolute; font-family: "Raleway", sans-serif; font-weight: 400;
    display: flex; align-items: center; gap: 10px;
  }
  .brand-nora { left: 52px; top: 1688px; font-size: 34px; color: #5d7a2e; }
  .brand-nora .dot { width: 22px; height: 22px; border-radius: 50%; background: #5d7a2e; }
  .brand-helena { left: 885px; top: 2022px; font-size: 26px; color: #8a1c1c; }

  .contact {
    left: 0; top: 2080px; width: 1200px; text-align: center;
    font-family: "Josefin Sans", sans-serif; font-weight: 300; font-size: 26px; line-height: 33px;
  }
  .contact p { margin: 0; }
  .contact strong { font-weight: 600; }
</style>
</head>
<body>
<div class="flyer">
  <svg class="shapes" width="1200" height="2200" viewBox="0 0 1200 2200">
    <defs>
      <linearGradient id="headerFill" x1="0" x2="1">
        <stop offset="0" stop-color="var(--blue-deep)"/>
        <stop offset="1" stop-color="#00c0cf"/>
      </linearGradient>
      <linearGradient id="footerFill" x1="0" x2="1">
        <stop offset="0" stop-color="var(--green-light)"/>
        <stop offset="0.5" stop-color="var(--teal)"/>
        <stop offset="1" stop-color="var(--teal)"/>
      </linearGradient>
      <linearGradient id="skyFill" x1="0" y1="0" x2="0.3" y2="1">
        <stop offset="0" stop-color="#2f6fb8"/>
        <stop offset="0.45" stop-color="#a9c8e6"/>
        <stop offset="0.75" stop-color="#8ea4b8"/>
        <stop offset="1" stop-color="#3f4d5c"/>
      </linearGradient>
      <linearGradient id="portraitWarm" x1="0" y1="0" x2="0" y2="1">
        <stop offset="0" stop-color="#7a3e2a"/>
        <stop offset="0.5" stop-color="#8c6a73"/>
        <stop offset="1" stop-color="#7d5c86"/>
      </linearGradient>
      <linearGradient id="portraitLight" x1="0" y1="0" x2="0" y2="1">
        <stop offset="0" stop-color="#f4f1ee"/>
        <stop offset="0.6" stop-color="#c9a895"/>
        <stop offset="1" stop-color="#222"/>
      </linearGradient>
      <path id="titleArc" d="M 50 560 A 388 388 0 0 1 660 290"/>
    </defs>

    <polygon class="header-band" points="0,0 1200,0 1105,183 0,183" fill="url(#headerFill)"/>

    <circle cx="435" cy="607" r="418" fill="var(--pale)"/>
    <circle cx="435" cy="607" r="360" fill="var(--blue)"/>
    <g role="img" aria-label="Photo of a climber hanging from a rope above mountains and clouds">
      <circle cx="440" cy="607" r="312" fill="url(#skyFill)"/>
    </g>
    <text fill="var(--cyan)" font-family="Nunito, sans-serif" font-weight="800" font-size="32">
      <textPath href="#titleArc">Rising above Hidden Career Deal breakers</textPath>
    </text>

    <circle cx="858" cy="790" r="333" fill="var(--pale)"/>
    <circle cx="858" cy="790" r="312" fill="var(--blue)"/>
    <path d="M 600 620 A 312 312 0 0 1 1170 790 A 312 312 0 0 1 1030 1050 L 858 790 Z" fill="var(--teal-dark)"/>
    <circle cx="858" cy="786" r="284" fill="var(--teal)" stroke="var(--white)" stroke-width="4"/>
    <circle cx="570" cy="651" r="21" fill="var(--teal)" stroke="var(--white)" stroke-width="4"/>

    <circle cx="837" cy="367" r="180" fill="var(--pale)"/>
    <circle cx="837" cy="367" r="150" fill="var(--teal)" stroke="var(--white)" stroke-width="4"/>

    <line x1="1072" y1="550" x2="1131" y2="492" stroke="var(--teal)" stroke-width="1.5"/>
    <line x1="578" y1="1075" x2="620" y2="1030" stroke="var(--teal)" stroke-width="1.5"/>
    <line x1="23" y1="776" x2="23" y2="914" stroke="var(--teal)" stroke-width="1.5"/>
    <line x1="1175" y1="1220" x2="1175" y2="1358" stroke="var(--blue)" stroke-width="1.5"/>
    <line x1="1162" y1="1370" x2="1162" y2="1508" stroke="var(--teal)" stroke-width="1.5"/>
    <line x1="24" y1="1560" x2="60" y2="1560" stroke="var(--teal)" stroke-width="1.5"/>

    <path class="blob-teal" fill="var(--teal)"
      d="M 24 1290 C 24 1230 40 1205 60 1195 L 460 1195 L 460 1250 C 560 1250 620 1200 700 1160 C 800 1110 960 1100 1060 1180 C 1150 1250 1180 1380 1140 1480 L 1105 1547 L 747 1547 L 747 1728 C 650 1720 600 1650 510 1640 L 460 1640 L 460 1380 L 60 1380 C 35 1360 24 1320 24 1290 Z"/>
    <path class="blob-blue" fill="var(--blue)"
      d="M 747 1728 C 650 1720 610 1638 505 1638 C 380 1638 290 1740 290 1860 C 290 1960 340 2020 400 2066 L 747 2066 Z"/>

    <g role="img" aria-label="Portrait photo of Dr. Nora Whitfield">
      <rect x="52" y="1137" width="408" height="515" fill="url(#portraitWarm)"/>
    </g>
    <g role="img" aria-label="Portrait photo of Dr. Helena Marchetti">
      <rect x="747" y="1547" width="410" height="468" fill="url(#portraitLight)"/>
    </g>

    <polygon class="footer-band" points="140,2066 1200,2066 1200,2200 28,2200" fill="url(#footerFill)"/>
  </svg>

  <div class="block hook">
    <p class="q">Is your career going the way you want?</p>
    <p class="feel">If not, do you feel <strong>STUCK? BLOCKED? FRUSTRATED?</strong></p>
    <p class="q">Don’t know what to do about this?</p>
  </div>

  <p class="block format"><strong>Format:</strong><br>4 Mini-Workshops +<br>2 short Online<br>Group Coaching<br>Sessions between<br>Workshops</p>

  <div class="block promise">
    <h2>Learn to overcome and rise<br>above the 4 top hidden career<br>deal breakers fast:</h2>
    <ul>
      <li>Microaggressions</li>
      <li>Toxic black box team dynamics</li>
      <li>Workplace snakes and other<br>dysfunctional types</li>
      <li>Disempowering subconscious<br>algorithms no matter what –<br>gedysfunctional subconscious<br>roles</li>
    </ul>
  </div>

  <h2 class="block section-title">Facilitators</h2>
  <div class="section-rule"></div>

  <div class="block bio-nora">
    <h3 class="bio-name">Dr. Nora Whitfield,</h3>
    <p class="bio-text">PhD, CPC, is an American &amp; Swiss-Trained Work &amp;<br>Organizational Psychologist, ICF-Certified Coach,<br>Board Certified Hypnotherapist, Certified Naturopath<br>(TEN) &amp; Certified Ayurvedic Practitioner.</p>
  </div>

  <div class="brand brand-nora"><span class="dot"></span>BrightPath</div>

  <div class="block bio-helena">
    <h3 class="bio-name">Dr. Helena Marchetti</h3>
    <p class="bio-text">Ph.D., PCC&nbsp; is a coach and<br>somatic experience practitioner<br>, a team coach with diploma<br>and a certified virtual team<br>coach.</p>
  </div>

  <div class="brand brand-helena">MarchettiCoaching</div>

  <div class="block contact">
    <p><strong>For&nbsp; dates, venue and further information contact Helena or Nora at:</strong></p>
    <p>Helena – helena@marchetticoaching.ch, <strong>079 000 12 34</strong>.</p>
    <p>Nora – nora@brightpath.ch, <strong>076 000 56 78</strong></p>
  </div>
</div>
</body>
</html>
```